Design a business card for Brenton's Heat Guardian
Brenton's Heat Guardian
Design a business card for Brenton's Heat Guardian - Food
Creative Brief
Traditional
Hal Brenton
President and CEO
52894 Corvane Lane Clinton Township, MI 48052
hbrenton1947@mailvex.example
www.brentonsheatguardian.example
Simple color marks, with some white space to write notes

```html
<!DOCTYPE html>
<html lang="en">
<head>
<meta charset="utf-8">
<title>Brenton's Heat Guardian — Business Card</title>
<link rel="stylesheet" href="https://fonts.googleapis.com/css2?family=Open+Sans:wght@400;600;700&display=swap">
<style>
  :root {
    --stage: #e4e4e4;
    --card: #ffffff;
    --ink: #1c1c1c;
    --muted: #444444;
    --orange: #f26a1b;
    --yellow: #f7c21a;
    --red: #e0301e;
    --ghost-a: #f1f1f1;
    --ghost-b: #e0e0e0;
  }
  * { box-sizing: border-box; margin: 0; padding: 0; }
  html, body {
    width: 1200px; height: 908px; overflow: hidden;
    background: var(--stage);
    font-family: "Open Sans", Arial, sans-serif;
  }
  .canvas {
    width: 1200px; height: 908px;
    display: flex; align-items: center; justify-content: center; gap: 60px;
  }
  .card {
    position: relative;
    width: 540px; height: 309px;
    background: var(--card);
    border-radius: 18px;
    overflow: hidden;
    box-shadow: 0 6px 18px rgba(0,0,0,.18);
  }
  .pot-art {
    position: absolute;
    border-radius: 36px 36px 56px 56px;
    background: linear-gradient(180deg, var(--ghost-a), var(--ghost-b));
    opacity: .7;
  }
  .card-front .pot-art { top: 22px; right: 26px; width: 190px; height: 150px; }
  .card-back .pot-art { top: 76px; right: 22px; width: 150px; height: 130px; }
  .brand-name {
    font-weight: 700; color: var(--ink);
    line-height: 1.1; letter-spacing: -.3px;
  }
  .brand-mark { width: 14px; height: 14px; background: var(--orange); flex: none; }
  /* front */
  .card-front .brand {
    position: absolute; left: 48px; bottom: 48px;
    display: flex; align-items: center; gap: 12px;
  }
  .card-front .brand-name { font-size: 26px; }
  /* back */
  .side-strip { position: absolute; left: 0; top: 0; width: 44px; height: 100%; }
  .strip-heat {
    position: absolute; left: 0; top: 0; width: 44px; height: 72px;
    background: linear-gradient(180deg, var(--red), var(--orange) 45%, var(--yellow));
  }
  .strip-band {
    position: absolute; left: 0; top: 150px; width: 44px; bottom: 0;
    background: linear-gradient(90deg, #000, #3a3a3a);
  }
  .card-back .brand {
    position: absolute; left: 64px; top: 96px;
    display: flex; align-items: center; gap: 10px;
  }
  .card-back .brand-name { font-size: 20px; }
  .person {
    position: absolute; right: 30px; top: 22px; text-align: right;
  }
  .person-name { font-size: 17px; font-weight: 600; color: var(--ink); }
  .person-title { font-size: 13px; font-weight: 600; color: var(--orange); margin-top: 2px; }
  .contact {
    position: absolute; left: 64px; top: 150px;
    list-style: none; font-size: 11.5px; color: var(--muted); line-height: 1.5;
  }
  .contact li { display: flex; align-items: center; gap: 7px; }
  .contact .address { display: block; margin-bottom: 6px; }
  .contact svg { width: 13px; height: 13px; flex: none; }
</style>
</head>
<body>
<main class="canvas">

  <section class="card card-front" aria-label="Card front">
    <div class="pot-art" role="img" aria-label="Faint cooking pot illustration"></div>
    <div class="brand">
      <span class="brand-mark"></span>
      <span class="brand-name">Brenton's Heat Guardian</span>
    </div>
  </section>

  <section class="card card-back" aria-label="Card back">
    <div class="pot-art" role="img" aria-label="Faint cooking pot illustration"></div>
    <div class="side-strip">
      <div class="strip-heat"></div>
      <div class="strip-band"></div>
    </div>
    <div class="person">
      <p class="person-name">Hal Brenton</p>
      <p class="person-title">President and CEO</p>
    </div>
    <div class="brand">
      <span class="brand-mark"></span>
      <span class="brand-name">Brenton's Heat Guardian</span>
    </div>
    <ul class="contact">
      <li class="address">52894 Corvane Lane<br>Harlow Springs, OH 44092</li>
      <li>
        <svg viewBox="0 0 16 16"><circle cx="8" cy="8" r="8" fill="#f26a1b"/><path d="M5 4.5l1.6-.4 1 2.2-1 .8a5 5 0 0 0 2.3 2.3l.8-1 2.2 1-.4 1.6c-3.6.2-6.7-2.9-6.5-6.5z" fill="#fff"/></svg>
        555-014-2290
      </li>
      <li>
        <svg viewBox="0 0 16 16"><circle cx="8" cy="8" r="8" fill="#f26a1b"/><path d="M5 4.5l1.6-.4 1 2.2-1 .8a5 5 0 0 0 2.3 2.3l.8-1 2.2 1-.4 1.6c-3.6.2-6.7-2.9-6.5-6.5z" fill="#fff"/></svg>
        555-018-7731
      </li>
      <li>
        <svg viewBox="0 0 16 16"><circle cx="8" cy="8" r="8" fill="#f26a1b"/><rect x="4" y="5" width="8" height="6" fill="none" stroke="#fff" stroke-width="1.2"/><path d="M4 5l4 3.5L12 5" fill="none" stroke="#fff" stroke-width="1.2"/></svg>
        hbrenton1947@mailvex.example
      </li>
      <li>
        <svg viewBox="0 0 16 16"><circle cx="8" cy="8" r="8" fill="#f26a1b"/><circle cx="8" cy="8" r="4" fill="none" stroke="#fff" stroke-width="1.1"/><path d="M4 8h8M8 4c-2 2.4-2 5.6 0 8M8 4c2 2.4 2 5.6 0 8" fill="none" stroke="#fff" stroke-width="1"/></svg>
        www.brentonsheatguardian.example
      </li>
    </ul>
  </section>

</main>
</body>
</html>
```